Business Card Design Project

We need a buisness card for a new digital sinage company. Our target cliants are small to mediaum buisness who want to advertise on out digital sinage network

Target Market(s)

Small to medium buisness

Industry/Entity Type

Digital

Requirements
Must have
• Must have logo

```html
<!DOCTYPE html>
<html lang="en">
<head>
<meta charset="utf-8">
<title>Vizo Business Card</title>
<link href="https://fonts.googleapis.com/css2?family=Jost:wght@400;500;700;800&display=swap" rel="stylesheet">
<style>
  :root {
    --page: #ece7df;
    --gold: #c9921a;
    --gold-light: #e6b53a;
    --gold-dark: #9a6a10;
    --ink: #1a1a1a;
    --paper: #ffffff;
    --accent-square: #8a5c0c;
  }
  * { margin: 0; padding: 0; box-sizing: border-box; }
  html, body {
    width: 1200px; height: 646px; overflow: hidden;
    background: var(--page);
    font-family: "Jost", sans-serif;
  }
  .canvas {
    position: relative; width: 1200px; height: 646px;
  }
  .card {
    position: absolute; top: 180px;
    width: 500px; height: 286px;
    border-radius: 14px; overflow: hidden;
    box-shadow: 0 6px 18px rgba(0,0,0,.18);
  }
  .card-back { left: 70px; }
  .card-front { left: 630px; background: var(--paper); }

  /* Back */
  .back-texture {
    position: absolute; inset: 0;
    background: radial-gradient(ellipse at 50% 30%, var(--gold-light) 0%, var(--gold) 55%, var(--gold-dark) 100%);
  }
  .back-brand {
    position: absolute; left: 0; right: 0; top: 92px;
    display: flex; justify-content: center; align-items: center; gap: 10px;
  }
  .brand-square {
    width: 26px; height: 26px; background: var(--paper);
  }
  .back-brand .brand-name {
    font-weight: 700; font-size: 40px; color: var(--paper); line-height: 1;
  }
  .back-web {
    position: absolute; left: 0; right: 0; top: 190px;
    text-align: center; color: var(--paper);
    font-size: 22px; font-weight: 400; letter-spacing: .5px;
  }

  /* Front */
  .front-shapes { position: absolute; inset: 0; }
  .front-name {
    position: absolute; right: 28px; top: 28px; text-align: right;
  }
  .person-name {
    font-weight: 800; font-size: 30px; color: var(--ink);
    text-transform: uppercase; letter-spacing: .5px; line-height: 1;
  }
  .person-role {
    font-size: 15px; color: var(--ink); margin-top: 2px;
  }
  .front-brand {
    position: absolute; left: 34px; top: 118px;
    display: flex; align-items: center; gap: 8px;
  }
  .front-brand .brand-square { background: var(--accent-square); width: 22px; height: 22px; }
  .front-brand .brand-name {
    font-weight: 700; font-size: 38px; color: var(--ink); line-height: 1;
  }
  .front-contact {
    position: absolute; right: 28px; top: 150px; text-align: right;
  }
  .contact-address {
    font-weight: 700; font-size: 18px; color: var(--gold);
  }
  .contact-email { font-size: 19px; color: var(--ink); margin-top: 2px; }
  .contact-phone { font-size: 22px; color: var(--ink); letter-spacing: .5px; }
</style>
</head>
<body>
<main class="canvas">

  <section class="card card-back">
    <div class="back-texture" role="img" aria-label="Gold background with a fine topographic contour pattern"></div>
    <div class="back-brand">
      <span class="brand-square"></span>
      <span class="brand-name">Vizo</span>
    </div>
    <p class="back-web">www.vizosign.com.au</p>
  </section>

  <section class="card card-front">
    <svg class="front-shapes" width="500" height="286" viewBox="0 0 500 286" aria-hidden="true">
      <defs>
        <linearGradient id="goldBand" x1="0" y1="0" x2="1" y2="0">
          <stop offset="0" stop-color="#e6b53a"/>
          <stop offset="1" stop-color="#c9921a"/>
        </linearGradient>
      </defs>
      <path d="M0 0 H500 V18 H60 Q28 18 28 50 V100 H0 Z" fill="url(#goldBand)"/>
      <path d="M0 200 H28 V250 Q28 268 46 268 H120 V286 H0 Z" fill="url(#goldBand)"/>
      <line x1="120" y1="118" x2="300" y2="80" stroke="#9a6a10" stroke-width="2"/>
      <line x1="300" y1="80" x2="472" y2="80" stroke="#9a6a10" stroke-width="2"/>
    </svg>
    <div class="front-name">
      <p class="person-name">Marcus Ellery</p>
      <p class="person-role">director</p>
    </div>
    <div class="front-brand">
      <span class="brand-square"></span>
      <span class="brand-name">Vizo</span>
    </div>
    <div class="front-contact">
      <p class="contact-address">PO Box 415 Karratha Bay WA 6799</p>
      <p class="contact-email">marcus@vizosign.com.au</p>
      <p class="contact-phone">0412555019</p>
    </div>
  </section>

</main>
</body>
</html>
```